Federal IT Consulting Company - Corvalen Advisory Partners

We're seeking a skilled web designer to create a modern, bold, and engaging WordPress website for Corvalen Advisory Partners, LLC. Our company specializes in federal IT consulting, and our name is a play on "Charting Circuitry." The website should reflect our expertise in the federal technology marketplace and position us as a trusted partner for clients navigating their IT journey.

contact: info@corvalenadv.example

Current Status

WordPress is already installed on our hosting account
We have an existing logo (may need modernization)

Design Requirements

Style:

Modern and visually striking design
Bold elements to convey confidence and expertise
Incorporate the concept of "charting circuitry" into the design

Features:

Modern UX sliders for dynamic content presentation
Eye-catching, high-quality images (stock photos to be sourced by the designer)
Responsive design for all devices

Color Scheme:

To be proposed by the designer, should align with our brand and convey trust and technological expertise

Logo:

Evaluate our current logo
Create a transparent background version if needed
Propose modernization if deemed necessary

Accessibility:

Ensure design elements are accessible to users with disabilities
Use high contrast ratios for text and background colors
Provide text alternatives for non-text content

Website Structure
Create the following pages, with the possibility of subpages:

Home
Services
About
Contact

Specific Page Requirements
Home Page

Striking hero section with a clear value proposition
Overview of our services
Client testimonials or trust indicators

Services Page

Detailed list of our IT consulting services
Clear explanation of how we help navigate the federal IT landscape

About Page

Company history and mission
Team highlights (if applicable)
Our approach to federal IT consulting

Contact Page

Contact form
Other contact methods (phone, email)

Technical Requirements

Fully responsive design
SEO best practices implemented
Fast loading times
Integration with necessary plugins (to be discussed)
Training on how to update and maintain the site
Full compliance with Web Content Accessibility Guidelines (WCAG) 2.1 Level AA
Adherence to Section 508 standards for federal website accessibility
Implementation of necessary features for ADA compliance

Target Market(s)

US Federal Govt customers looking for IT support.

Industry/Entity Type

IT Consulting

Coding

Coded - Design and coding required

Colors
0054AA
0677BA
7BADD7
CADEEF
E8F1F8
0094D4
00A9DD
6FCCEA
C7EBF8
E9F6FB
00AB8E
00BBA5
67D7C9
C6EFE9
E9F9F6

```html
<!DOCTYPE html>
<html lang="en">
<head>
<meta charset="utf-8">
<title>Corvalen Advisory Partners</title>
<link href="https://fonts.googleapis.com/css2?family=Poppins:wght@300;400;500;600;700&display=swap" rel="stylesheet">
<style>
:root{
  --brand:#0094d4;
  --brand-bright:#00a9dd;
  --brand-soft:#6fccea;
  --sky:#e9f6fb;
  --sky-mid:#c7ebf8;
  --ink:#2e2e33;
  --body:#3a3a40;
  --muted:#77787d;
  --footer:#3a3b40;
  --white:#ffffff;
  --violet:#7b6fd0;
  --star:#f5a623;
}
*{margin:0;padding:0;box-sizing:border-box}
html,body{width:1200px;height:4515px;overflow:hidden}
body{font-family:'Poppins',sans-serif;color:var(--body);background:var(--white);position:relative}
.abs{position:absolute}
a{color:inherit;text-decoration:none}

/* header */
.site-header{position:absolute;left:0;top:0;width:1200px;height:123px;background:var(--white)}
.brand-name{position:absolute;left:74px;top:34px;font-size:34px;font-weight:700;color:var(--ink);letter-spacing:1px}
.main-nav{position:absolute;right:74px;top:42px;display:flex;align-items:center;gap:40px;font-size:13px;color:var(--ink)}
.nav-cta{background:var(--brand);color:var(--white);padding:9px 16px;border-radius:20px}

/* hero */
.hero{position:absolute;left:0;top:123px;width:1200px;height:690px}
.hero-title{position:absolute;left:72px;top:132px;font-size:72px;font-weight:700;color:var(--ink);letter-spacing:3px}
.hero-text{position:absolute;left:74px;top:258px;width:510px;font-size:16px;line-height:25px;color:var(--ink)}
.btn{position:absolute;display:flex;align-items:center;gap:14px;height:58px;padding:0 24px;border-radius:30px;background:var(--brand);color:var(--white);font-size:17px;font-weight:400}
.hero-art{position:absolute;left:587px;top:70px;width:613px;height:570px;border-radius:45% 30% 40% 50%;background:linear-gradient(150deg,#a89ee6,var(--violet) 55%,#5a4fb8)}

/* section heads */
.section-head{position:absolute;text-align:left}
.section-head h2{font-size:44px;font-weight:600;color:var(--ink);line-height:1}
.section-head p{font-size:24px;font-weight:600;color:var(--brand);letter-spacing:3px;text-align:right;margin-top:4px}

/* service cards */
.service-card{position:absolute;width:316px;height:287px;background:var(--white);border-radius:10px;box-shadow:0 2px 12px rgba(0,0,0,.12);text-align:center;padding-top:26px}
.service-card.is-active{border:2px solid var(--brand)}
.service-icon{display:block;margin:0 auto}
.service-card h3{margin-top:14px;font-size:17px;font-weight:400;color:var(--brand)}
.service-card p{margin:16px auto 0;width:240px;font-size:13px;line-height:22px;color:var(--body)}

/* why choose */
.why-photo{position:absolute;left:0;top:1892px;width:526px;height:790px;border-radius:0 50% 50% 0;background:linear-gradient(135deg,#c9d3db,#7f8c99 50%,#dfe6ec)}
.why-item{position:absolute;display:flex;align-items:center;gap:16px;font-size:18px;color:var(--ink)}
.why-circle{width:118px;height:118px;border-radius:50%;background:var(--white);box-shadow:0 0 14px rgba(0,148,212,.25);display:flex;align-items:center;justify-content:center}
.why-blob{position:absolute;left:858px;top:1953px;width:420px;height:500px;border-radius:60% 0 0 55%;background:var(--sky)}
.why-text{position:absolute;right:74px;top:2095px;text-align:right}
.why-text h2{font-size:44px;font-weight:500;color:var(--ink);line-height:54px}
.why-text .accent{font-size:26px;font-weight:600;color:var(--brand);letter-spacing:3px}
.why-text p{margin-top:24px;width:250px;margin-left:auto;font-size:13px;line-height:22px}
.why-text .rule{width:64px;height:2px;background:var(--brand);margin:30px 0 0 auto}

/* about */
.about-text{position:absolute;left:74px;top:3018px;width:440px;font-size:13px;line-height:24px}
.photo{position:absolute;border-radius:8px}

/* testimonials */
.quote-card{position:absolute;width:319px;height:245px;background:var(--white);border-radius:18px;box-shadow:0 2px 14px rgba(0,0,0,.1);padding:56px 38px 0}
.quote-card p{font-size:15px;line-height:22px;text-align:justify;color:var(--body)}
.quote-mark{position:absolute;right:34px;top:18px;font-size:90px;line-height:1;color:#e4e4e6;font-weight:700;font-family:Georgia,serif}
.quote-foot{position:absolute;left:38px;right:38px;top:184px;border-top:1px solid #e2e2e2;padding-top:10px;display:flex;justify-content:space-between}
.quote-foot b{display:block;font-size:13px;font-weight:600;color:var(--ink)}
.quote-foot small{font-size:9px;color:var(--muted)}
.stars{color:var(--star);font-size:12px;letter-spacing:1px}
.avatar{position:absolute;width:66px;height:66px;border-radius:50%;background:linear-gradient(135deg,#d8c7b5,#8d7b6b);border:3px solid var(--white)}
.dots{position:absolute;left:570px;top:3973px;display:flex;gap:14px}
.dots span{width:11px;height:11px;border-radius:50%;background:var(--sky-mid)}
.dots span.on{background:var(--brand)}

/* footer */
.site-footer{position:absolute;left:0;top:4050px;width:1200px;height:465px}
.footer-col{position:absolute;color:var(--white);font-size:13px}
.footer-col h4{font-size:17px;font-weight:500;color:var(--brand);}
.footer-col .bar{width:34px;height:2px;background:var(--white);margin:12px 0 24px}
.footer-col li{list-style:none;margin-bottom:10px;display:flex;align-items:center;gap:6px}
.link-dot{width:12px;height:12px;border:1.5px solid var(--brand);border-radius:50%}
.contact-row{display:flex;gap:16px;align-items:flex-start;margin-bottom:18px;line-height:16px}
.contact-icon{width:26px;height:26px;border:1px solid var(--brand);border-radius:4px;display:flex;align-items:center;justify-content:center;flex:none}
.newsletter-field{margin-top:22px;width:213px;height:36px;border:1px solid var(--brand);border-radius:20px;display:flex;align-items:center;justify-content:space-between;padding:0 6px 0 16px;font-size:11px;color:#b8b9bd}
.social{position:absolute;left:118px;top:4357px;display:flex;gap:12px}
.social span{width:30px;height:30px;border:1.5px solid var(--brand);border-radius:3px}
.copyright{position:absolute;left:0;top:4459px;width:1200px;height:56px;background:var(--brand);color:var(--white);font-size:12px;text-align:center;line-height:56px}
</style>
</head>
<body>

<header class="site-header">
  <div class="brand-name">CORVALEN</div>
  <nav class="main-nav">
    <a href="#">HOME</a><a href="#">SERVICES</a><a href="#">ABOUT</a><a href="#">BLOG</a><a href="#" class="nav-cta">CONTACT</a>
  </nav>
</header>

<section class="hero">
  <svg class="abs" style="left:0;top:0" width="1200" height="690" viewBox="0 0 1200 690">
    <path d="M0 0H1200V580C1050 640 900 690 700 680C450 670 200 560 0 600Z" fill="#e9f6fb"/>
  </svg>
  <h1 class="hero-title">CORVALEN</h1>
  <p class="hero-text">Lorem ipsum dolor sit amet, consectetur adipiscing elit, sed do eiusmod tempor incididunt ut labore et dolore magna</p>
  <a href="#" class="btn" style="left:74px;top:350px">GET STARTED
    <svg width="30" height="12" viewBox="0 0 30 12"><path d="M0 6H28M22 1L28 6L22 11" stroke="#fff" stroke-width="2" fill="none"/></svg></a>
  <div class="hero-art" role="img" aria-label="Illustration of a consultant working at a laptop beside a desk with plants, connected to colleague avatars over a city skyline"></div>
</section>

<div class="section-head" style="left:460px;top:912px">
  <h2>OUR SERVICES</h2><p>WHAT WE DO</p>
</div>

<!-- service cards -->
<div class="service-card" style="left:84px;top:1081px">
  <svg class="service-icon" width="96" height="96" viewBox="0 0 96 96"><circle cx="48" cy="48" r="44" fill="none" stroke="#0094d4" stroke-width="6"/><circle cx="48" cy="48" r="30" fill="#0094d4"/><rect x="32" y="36" width="32" height="24" rx="2" fill="none" stroke="#fff" stroke-width="2"/><path d="M42 44L38 48L42 52M54 44L58 48L54 52" stroke="#fff" stroke-width="2" fill="none"/></svg>
  <h3>APPLICATION DESIGN</h3>
  <p>Lorem ipsum dolor sit amet, conse ctetur adipiscing elit, sed do eiusmod tempor</p>
</div>
<div class="service-card is-active" style="left:438px;top:1081px">
  <svg class="service-icon" width="96" height="96" viewBox="0 0 96 96"><circle cx="48" cy="48" r="44" fill="none" stroke="#0094d4" stroke-width="6"/><circle cx="48" cy="48" r="30" fill="#0094d4"/><rect x="36" y="34" width="24" height="8" rx="2" fill="none" stroke="#fff" stroke-width="2"/><rect x="36" y="44" width="24" height="8" rx="2" fill="none" stroke="#fff" stroke-width="2"/><path d="M48 52V62M40 62H56" stroke="#fff" stroke-width="2"/></svg>
  <h3>WEB HOSTING</h3>
  <p>Lorem ipsum dolor sit amet, conse ctetur adipiscing elit, sed do eiusmod tempor</p>
</div>
<div class="service-card" style="left:797px;top:1081px">
  <svg class="service-icon" width="96" height="96" viewBox="0 0 96 96"><circle cx="48" cy="48" r="44" fill="none" stroke="#0094d4" stroke-width="6"/><circle cx="48" cy="48" r="30" fill="#0094d4"/><circle cx="48" cy="44" r="10" fill="none" stroke="#fff" stroke-width="2"/><path d="M34 62C38 54 58 54 62 62" stroke="#fff" stroke-width="2" fill="none"/></svg>
  <h3>APPLICATION DESIGN</h3>
  <p>Lorem ipsum dolor sit amet, conse ctetur adipiscing elit, sed do eiusmod tempor</p>
</div>
<div class="service-card" style="left:84px;top:1398px">
  <svg class="service-icon" width="96" height="96" viewBox="0 0 96 96"><circle cx="48" cy="48" r="44" fill="none" stroke="#0094d4" stroke-width="6"/><circle cx="48" cy="48" r="30" fill="#0094d4"/><circle cx="48" cy="48" r="13" fill="none" stroke="#fff" stroke-width="2" stroke-dasharray="5 3"/><path d="M45 44L42 48L45 52M51 44L54 48L51 52" stroke="#fff" stroke-width="2" fill="none"/></svg>
  <h3>SEO OPTIMIZATION</h3>
  <p>Lorem ipsum dolor sit amet, conse ctetur adipiscing elit, sed do eiusmod tempor</p>
</div>
<div class="service-card" style="left:438px;top:1398px">
  <svg class="service-icon" width="96" height="96" viewBox="0 0 96 96"><circle cx="48" cy="48" r="44" fill="none" stroke="#0094d4" stroke-width="6"/><circle cx="48" cy="48" r="30" fill="#0094d4"/><circle cx="45" cy="45" r="10" fill="none" stroke="#fff" stroke-width="2"/><path d="M52 52L62 62" stroke="#fff" stroke-width="3"/></svg>
  <h3>DIGITAL MARKETING</h3>
  <p>Lorem ipsum dolor sit amet, conse ctetur adipiscing elit, sed do eiusmod tempor</p>
</div>
<div class="service-card" style="left:797px;top:1398px">
  <svg class="service-icon" width="96" height="96" viewBox="0 0 96 96"><circle cx="48" cy="48" r="44" fill="none" stroke="#0094d4" stroke-width="6"/><circle cx="48" cy="48" r="30" fill="#0094d4"/><rect x="39" y="46" width="18" height="14" rx="2" fill="none" stroke="#fff" stroke-width="2"/><path d="M42 46V41A6 6 0 0 1 54 41V46" stroke="#fff" stroke-width="2" fill="none"/></svg>
  <h3>DATA SECURITY</h3>
  <p>Lorem ipsum dolor sit amet, conse ctetur adipiscing elit, sed do eiusmod tempor</p>
</div>

<!-- why choose -->
<div class="why-photo" role="img" aria-label="Photo of a business team meeting around a glass conference table in a bright office"></div>
<div class="why-blob"></div>

<div class="why-item" style="left:512px;top:1903px"><div class="why-circle"><svg width="60" height="60" viewBox="0 0 60 60"><circle cx="30" cy="30" r="26" fill="none" stroke="#0094d4" stroke-width="2"/><text x="30" y="39" text-anchor="middle" font-size="26" fill="#0094d4" font-family="Poppins,sans-serif">$</text></svg></div>Pricing</div>
<div class="why-item" style="left:616px;top:2057px"><div class="why-circle"><svg width="60" height="60" viewBox="0 0 60 60"><path d="M30 8L52 18V42L30 52L8 42V18Z M8 18L30 28L52 18 M30 28V52" fill="none" stroke="#0094d4" stroke-width="2"/></svg></div>Delivery</div>
<div class="why-item" style="left:637px;top:2227px"><div class="why-circle"><svg width="60" height="60" viewBox="0 0 60 60"><circle cx="30" cy="24" r="10" fill="none" stroke="#0094d4" stroke-width="2"/><path d="M16 26V22A14 14 0 0 1 44 22V26M12 52C14 40 46 40 48 52" fill="none" stroke="#0094d4" stroke-width="2"/></svg></div>Support</div>
<div class="why-item" style="left:607px;top:2397px"><div class="why-circle"><svg width="60" height="60" viewBox="0 0 60 60"><circle cx="26" cy="30" r="14" fill="none" stroke="#0094d4" stroke-width="2" stroke-dasharray="6 3"/><circle cx="26" cy="30" r="5" fill="none" stroke="#0094d4" stroke-width="2"/><path d="M38 40L43 45L52 34" fill="none" stroke="#0094d4" stroke-width="2"/></svg></div>Experience</div>
<div class="why-item" style="left:502px;top:2544px"><div class="why-circle"><svg width="60" height="60" viewBox="0 0 60 60"><circle cx="28" cy="32" r="14" fill="none" stroke="#0094d4" stroke-width="2" stroke-dasharray="6 3"/><rect x="32" y="10" width="8" height="16" rx="3" fill="none" stroke="#0094d4" stroke-width="2"/><path d="M22 32L26 36L34 28" fill="none" stroke="#0094d4" stroke-width="2"/></svg></div>Products</div>

<div class="why-text">
  <h2>WHY<br>CHOOSE</h2>
  <div class="accent">CORVALEN</div>
  <p>Lorem ipsum dolor sit amet, conse ctetur adipiscing elit, sed do eiusmod tempor</p>
  <div class="rule"></div>
</div>

<!-- about -->
<div class="section-head" style="left:120px;top:2888px">
  <h2>ABOUT US</h2><p>WHO WE ARE</p>
</div>
<p class="about-text">Lorem ipsum dolor sit amet, conse ctetur adipiscing elit, sed do eiusmod tempor incididunt ut labore et dolore magna aliqua. Ut enim ad minim veniam, quis nostrud exercitation ullamco laboris nisi ut aliquip ex ea commodo consequat</p>
<a href="#" class="btn" style="left:74px;top:3159px">KNOW MORE
  <svg width="30" height="12" viewBox="0 0 30 12"><path d="M0 6H28M22 1L28 6L22 11" stroke="#fff" stroke-width="2" fill="none"/></svg></a>
<div class="photo" style="left:583px;top:2847px;width:260px;height:441px;background:linear-gradient(160deg,#1d4a78,#2f6d9c 50%,#0f2d4e)" role="img" aria-label="Photo of a consultant working on a laptop surrounded by digital data overlays"></div>
<div class="photo" style="left:862px;top:2810px;width:261px;height:244px;background:linear-gradient(150deg,#f2f4f6,#c9ced3)" role="img" aria-label="Photo of hands pointing at a tablet beside a laptop on a white desk"></div>
<div class="photo" style="left:862px;top:3075px;width:261px;height:241px;background:linear-gradient(150deg,#9aa8b6,#4b5663)" role="img" aria-label="Photo of a team gathered around a tablet in an office"></div>

<!-- testimonials -->
<div class="section-head" style="left:470px;top:3470px">
  <h2>TESTIMONIALS</h2><p>CLIENT REVIEWS</p>
</div>

<div class="quote-card" style="left:70px;top:3653px">
  <span class="quote-mark">&ldquo;</span>
  <p>Lorem ipsum dolor sit amet, conse ctetuer adipiscing elit. Aenean comodo ligula eget dolor. Aenean massa. Cum sociis</p>
  <div class="quote-foot"><div><b>Marcus Ellery</b><small>Managing Director</small></div><span class="stars">★★★★★</span></div>
</div>
<div class="avatar" style="left:104px;top:3620px" role="img" aria-label="Client portrait"></div>

<div class="quote-card" style="left:436px;top:3653px">
  <span class="quote-mark">&ldquo;</span>
  <p>Lorem ipsum dolor sit amet, conse ctetuer adipiscing elit. Aenean comodo ligula eget dolor. Aenean massa. Cum sociis</p>
  <div class="quote-foot"><div><b>Marcus Ellery</b><small>Managing Director</small></div><span class="stars">★★★★★</span></div>
</div>
<div class="avatar" style="left:470px;top:3620px;background:linear-gradient(135deg,#e6e6e6,#9a9a9a)" role="img" aria-label="Client portrait"></div>

<div class="quote-card" style="left:802px;top:3653px">
  <span class="quote-mark">&ldquo;</span>
  <p>Lorem ipsum dolor sit amet, conse ctetuer adipiscing elit. Aenean comodo ligula eget dolor. Aenean massa. Cum sociis</p>
  <div class="quote-foot"><div><b>Marcus Ellery</b><small>Managing Director</small></div><span class="stars">★★★★★</span></div>
</div>
<div class="avatar" style="left:836px;top:3620px;background:linear-gradient(135deg,#b98a6a,#5a3b2a)" role="img" aria-label="Client portrait"></div>

<div class="dots"><span></span><span></span><span class="on"></span></div>

<!-- footer -->
<footer class="site-footer">
  <svg class="abs" style="left:0;top:0" width="1200" height="409" viewBox="0 0 1200 409">
    <path d="M0 90C200 30 420 0 640 8C860 16 1050 70 1200 100V409H0Z" fill="#3a3b40"/>
  </svg>
  <div class="footer-col" style="left:74px;top:205px"><div style="font-size:34px;font-weight:700;color:#fff;letter-spacing:1px">CORVALEN</div></div>
  <div class="footer-col" style="left:396px;top:140px">
    <h4>QUICK LINKS</h4><div class="bar"></div>
    <ul><li><span class="link-dot"></span>Home</li><li><span class="link-dot"></span>Services</li><li><span class="link-dot"></span>About</li><li><span class="link-dot"></span>Blog</li><li><span class="link-dot"></span>Contact Us</li></ul>
  </div>
  <div class="footer-col" style="left:603px;top:140px">
    <h4>CONTACT US</h4><div class="bar"></div>
    <div class="contact-row"><span class="contact-icon"><svg width="12" height="12" viewBox="0 0 12 12"><path d="M2 1L4 1L5 4L3.5 5C4 6.5 5.5 8 7 8.5L8 7L11 8V10C11 10.5 10.5 11 10 11C5 11 1 7 1 2C1 1.5 1.5 1 2 1Z" fill="none" stroke="#0094d4"/></svg></span><div>CALL US<br>555 010 2417</div></div>
    <div class="contact-row"><span class="contact-icon"><svg width="12" height="10" viewBox="0 0 12 10"><rect x=".5" y=".5" width="11" height="9" fill="none" stroke="#0094d4"/><path d="M.5 .5L6 5L11.5 .5" fill="none" stroke="#0094d4"/></svg></span><div>EMAIL US<br>info@corvalenadv.example</div></div>
    <div class="contact-row"><span class="contact-icon"><svg width="10" height="13" viewBox="0 0 10 13"><path d="M5 12C5 12 1 7 1 4.5A4 4 0 0 1 9 4.5C9 7 5 12 5 12Z" fill="none" stroke="#0094d4"/><circle cx="5" cy="4.5" r="1.4" fill="#0094d4"/></svg></span><div>Address line Dummy Here<br>Address line Here</div></div>
  </div>
  <div class="footer-col" style="left:894px;top:140px">
    <h4>OUR NEWSLETTER</h4><div class="bar"></div>
    <div style="width:220px;line-height:17px">Subscribe our newsletter to get the latest news.</div>
    <div class="newsletter-field" style="margin-left:-7px">Enter Email Address<svg width="26" height="26" viewBox="0 0 26 26"><circle cx="13" cy="13" r="11" fill="none" stroke="#0094d4" stroke-width="1.5"/><path d="M8 13H18M14 9L18 13L14 17" fill="none" stroke="#0094d4" stroke-width="1.5"/></svg></div>
  </div>
</footer>
<div class="social"><span></span><span></span><span></span><span></span></div>
<div class="copyright">Copyright © 2024 All Rights Reserved By Company name</div>

</body>
</html>
```